Digital Recipe eBook Design

I need a recipe eBook designed for me. I have attached the recipes (see here https://files.plomvara.net/doc/7Kp2RtQx9LmZw4YbVn3HsJd8FgTc6XeA1uNo5WiEqBr/view) and associated images in Plomvara Files (see images here https://files.plomvara.net/set/83TbWqzLmNpo2VxYcRk6HsJ?view). I am open to any sort of ideas but want the recipe book to look highly professional and with a simple, yet sleek, design. I have included some examples of designs I like here: https://files.plomvara.net/set/5R_Qx2MbVtZk9YwLpHnCdFs?view

Target Market(s)

Women 20-35

Industry/Entity Type

Health And Wellness

Font styles to use
Sans Serif

Colors
e667a6
eea4c8
f9deeb

Requirements
Must have
• No typos
• Professional design
Should not have
• Overly decorative design - keep it simple and clean

```html
<!DOCTYPE html>
<html lang="en">
<head>
<meta charset="utf-8">
<title>Breakfast Recipe eBook Pages</title>
<link href="https://fonts.googleapis.com/css2?family=Didact+Gothic&family=Montserrat:wght@400;500&display=swap" rel="stylesheet">
<style>
  :root {
    --pink-strong: #e667a6;
    --pink-mid: #eea4c8;
    --pink-soft: #f9deeb;
    --backdrop: #b3b3b3;
    --paper: #ffffff;
    --ink: #5a5a5a;
    --photo-bowl: linear-gradient(135deg, #4f8a2c 0%, #cfd9a8 35%, #e9e6d6 50%, #e07a3a 70%, #c9d46a 100%);
  }
  * { margin: 0; padding: 0; box-sizing: border-box; }
  html, body { width: 1200px; height: 675px; overflow: hidden; background: var(--backdrop); }
  body { position: relative; font-family: "Montserrat", sans-serif; color: var(--ink); }

  .page {
    position: absolute; top: 138px; height: 338px;
    background: var(--paper); overflow: hidden;
    box-shadow: 0 1px 4px rgba(0,0,0,0.15);
  }
  .page::after {
    content: ""; position: absolute; left: 0; right: 0; bottom: 0; height: 8px;
    background: var(--pink-mid);
  }
  .page--cover { left: 61px; width: 263px; }
  .page--recipe { left: 341px; width: 263px; }
  .page--feature { left: 624px; width: 261px; }
  .page--feature-pink { left: 906px; width: 262px; }

  .photo { position: absolute; }
  .photo--bowl { background: var(--photo-bowl); }
  .photo--smoothie { background: linear-gradient(160deg, #f2f2ee 0%, #c9b3a0 55%, #5b3a2a 100%); }
  .photo--muffins { background: linear-gradient(135deg, #6e6e6e 0%, #e39a3c 45%, #d9612f 70%, #777 100%); }
  .photo--juice { background: linear-gradient(170deg, #8a8aa0 0%, #b7c77a 50%, #7fae2d 100%); }

  /* Cover */
  .cover-grid .photo { width: 95px; height: 84px; }
  .cover-title-frame {
    position: absolute; left: 59px; top: 139px; width: 145px; height: 50px;
    border: 1px solid var(--pink-mid);
  }
  .cover-title {
    position: absolute; left: 69px; top: 149px; width: 125px; height: 31px;
    background: var(--pink-mid); color: #fff;
    font-family: "Didact Gothic", sans-serif; font-size: 27px; line-height: 31px;
    text-align: center;
  }

  /* Recipe */
  .recipe-header { left: 0; top: 0; width: 100%; height: 49px; }
  .recipe-title-frame {
    position: absolute; left: 51px; top: 7px; width: 152px; height: 36px;
    border: 1px solid var(--pink-mid);
  }
  .recipe-title {
    position: absolute; left: 59px; top: 14px; width: 141px; height: 24px;
    background: var(--pink-mid); color: #fff;
    font-family: "Didact Gothic", sans-serif; font-size: 12.5px; line-height: 24px; text-align: center;
  }
  .recipe-thumb { left: 22px; top: 76px; width: 105px; height: 68px; }
  .serves {
    position: absolute; left: 22px; top: 151px;
    font-family: "Didact Gothic", sans-serif; font-size: 5.5px; color: var(--pink-strong);
  }
  .section-heading {
    position: absolute; font-family: "Didact Gothic", sans-serif;
    font-size: 12px; color: var(--pink-strong); font-weight: 400;
  }
  .section-heading--ingredients { left: 142px; top: 69px; }
  .section-heading--method { left: 22px; top: 180px; }
  .ingredients {
    position: absolute; left: 150px; top: 90px; width: 90px;
    font-size: 5.8px; line-height: 9.4px; letter-spacing: 0.2px; list-style: none;
  }
  .ingredients li { position: relative; }
  .ingredients li::before {
    content: ""; position: absolute; left: -6px; top: 3.6px;
    width: 2px; height: 2px; border-radius: 50%; background: var(--ink);
  }
  .method {
    position: absolute; left: 21px; top: 208px; width: 216px;
    font-size: 5.3px; line-height: 8.7px; letter-spacing: 0.15px;
    list-style: none; counter-reset: step;
  }
  .method li { counter-increment: step; padding-left: 5px; position: relative; }
  .method li::before { content: counter(step) "."; position: absolute; left: 0; }

  /* Feature pages */
  .feature-photo { left: 0; top: 0; width: 100%; height: 221px; }
  .feature-text {
    position: absolute; left: 28px; width: 206px;
    font-size: 4.6px; line-height: 8px; letter-spacing: 0.3px; text-align: justify;
  }
  .feature-text ul { list-style: none; margin-top: 6px; }
  .feature-text li { position: relative; padding-left: 6px; }
  .feature-text li::before {
    content: ""; position: absolute; left: 0; top: 3.4px;
    width: 1.6px; height: 1.6px; border-radius: 50%; background: currentColor;
  }
  .feature-note { text-align: center; margin-top: 8px; }
  .page--feature .feature-text { top: 234px; }
  .page--feature .feature-note { color: var(--pink-strong); }
  .pink-panel {
    position: absolute; left: 0; top: 221px; width: 100%; bottom: 0;
    background: var(--pink-strong);
  }
  .page--feature-pink::after { display: none; }
  .page--feature-pink .feature-text { top: 237px; color: #fff; }
</style>
</head>
<body>

  <section class="page page--cover">
    <div class="cover-grid">
      <div class="photo photo--bowl" style="left:34px;top:78px" role="img" aria-label="Breakfast bowl with spinach, eggs, cauliflower, avocado and sweet potato"></div>
      <div class="photo photo--smoothie" style="left:134px;top:78px;width:94px" role="img" aria-label="Hand holding a glass of chocolate smoothie"></div>
      <div class="photo photo--muffins" style="left:34px;top:166px" role="img" aria-label="Baked egg muffins on a cooling rack"></div>
      <div class="photo photo--juice" style="left:134px;top:166px;width:94px" role="img" aria-label="Two bottles of green juice with white flowers"></div>
    </div>
    <div class="cover-title-frame"></div>
    <h1 class="cover-title">Breakfast</h1>
  </section>

  <section class="page page--recipe">
    <div class="photo photo--bowl recipe-header" role="img" aria-label="Close-up of the breakfast bowl on marble"></div>
    <div class="recipe-title-frame"></div>
    <h2 class="recipe-title">Goddess Breakfast Bowl</h2>
    <div class="photo photo--bowl recipe-thumb" role="img" aria-label="Goddess breakfast bowl from above"></div>
    <p class="serves">Serves 1</p>

    <h3 class="section-heading section-heading--ingredients">Ingredients</h3>
    <ul class="ingredients">
      <li>2 eggs (free range or organic where possible)</li>
      <li>¼ avocado</li>
      <li>½ small sweet potato, cubed (around ½ cup)</li>
      <li>2 florets of cauliflower</li>
      <li>Large handful of fresh greens (e.g. baby spinach)</li>
      <li>Drizzle of olive oil</li>
    </ul>

    <h3 class="section-heading section-heading--method">How To:</h3>
    <ol class="method">
      <li>Boil a small saucepan of water and once boiling gently add the two eggs and set a timer for 6 minutes (for soft-boiled) or 10 minutes (for hard-boiled)</li>
      <li>Meanwhile, steam the sweet potato and cauliflower until just soft</li>
      <li>When the eggs are done, remove from the saucepan and place in an ice-cold bowl of water for 2-3 minutes (this makes the eggs easier to peel)</li>
      <li>Remove the eggs from the water and peel away their shells</li>
      <li>Assemble the bowl: place the greens at the bottom and top with eggs, sweet potato, cauliflower and avocado</li>
      <li>Garnish with salt and pepper and a drizzle of olive oil</li>
      <li>Enjoy!</li>
    </ol>
  </section>

  <section class="page page--feature">
    <div class="photo photo--bowl feature-photo" role="img" aria-label="Full-page photo of the goddess breakfast bowl"></div>
    <div class="feature-text">
      <p>This bowl is the ultimate balanced breakfast for your hormones that will keep you full all morning. Start your day by ticking all the hormone-balancing principals in one bowl:</p>
      <ul>
        <li>Healthy fats from avocado, egg yolks and olive oil</li>
        <li>Protein from eggs</li>
        <li>Complex carbohydrates from sweet potato</li>
        <li>Liver and cycle-supporting nutrients from cauliflower and greens</li>
      </ul>
      <p class="feature-note">NOTE: This bowl can be prepared the night before for an easy grab-and-go breakfast</p>
    </div>
  </section>

  <section class="page page--feature-pink">
    <div class="photo photo--bowl feature-photo" role="img" aria-label="Full-page photo of the goddess breakfast bowl"></div>
    <div class="pink-panel"></div>
    <div class="feature-text">
      <p>This bowl is the ultimate balanced breakfast for your hormones that will keep you full all morning. Start your day by ticking all the hormone-balancing principals in one bowl:</p>
      <ul>
        <li>Healthy fats from avocado, egg yolks and olive oil</li>
        <li>Protein from eggs</li>
        <li>Complex carbohydrates from sweet potato</li>
        <li>Liver and cycle-supporting nutrients from cauliflower and greens</li>
      </ul>
      <p class="feature-note">NOTE: This bowl can be prepared the night before for an easy grab-and-go breakfast</p>
    </div>
  </section>

</body>
</html>
```